Web Design For Metal Recycling Company

We are a scrap and recycling company dealing mainly in scrap metal base in Singapore. We deal in both domestic market and international market. Currently we are still unsure if we want to have a "lively" or "professional" company image so we will leave it to the designer to deem what is good.

We wish for a website to be able to "Retain" the interest of new visitor and at the same time able to give enough information for new and existing customer. We would also wish for design that will get the visitor to "Engage" us.

The attached is the logo for the company and we would want to incorporate that into the website. Either of the logo is fine.

```html
<!DOCTYPE html>
<html lang="en">
<head>
<meta charset="utf-8">
<title>Keng Hoe Metals</title>
<link href="https://fonts.googleapis.com/css2?family=Open+Sans:wght@400;600;700;800&display=swap" rel="stylesheet">
<style>
:root{
  --navy:#2e3e50;
  --navy-dark:#26333f;
  --red:#d3454a;
  --red-dark:#b93a3f;
  --page:#f6f6f6;
  --band:#ebebeb;
  --white:#ffffff;
  --text:#555b61;
  --muted:#8a9096;
  --line:#dcdcdc;
}
*{box-sizing:border-box;margin:0;padding:0}
html,body{width:900px;height:1200px;overflow:hidden}
body{position:relative;background:var(--page);font-family:"Open Sans",Arial,sans-serif;color:var(--text);font-size:8px}
.abs{position:absolute}
.section-bar{position:absolute;left:158px;width:584px;height:29px;background:var(--navy);color:#fff;font-weight:800;font-size:13px;letter-spacing:.3px;padding:6px 16px;text-transform:uppercase}
.section-bar.red{background:var(--red)}
.section-bar .toggle{position:absolute;right:8px;top:8px;width:13px;height:13px;background:rgba(255,255,255,.18)}
.band-grey{position:absolute;left:0;top:336px;width:900px;height:378px;background:var(--band)}
/* services */
.services{position:absolute;left:158px;top:60px;width:584px;display:flex}
.service{width:97.3px;text-align:center}
.service svg{width:26px;height:22px}
.service h3{color:var(--red);font-weight:600;font-size:10.5px;margin:12px 0 7px}
.service p{font-size:6px;line-height:9px;color:var(--muted);text-align:left;padding:0 2px}
/* tabs */
.tabs{position:absolute;left:158px;top:189px;display:flex}
.tab{font-size:9px;font-weight:600;padding:4px 7px;background:#e4e4e4;color:var(--text);margin-right:2px}
.tab.active{background:var(--white);color:var(--red)}
.tab-panel{position:absolute;left:158px;top:208px;width:282px;height:97px;background:var(--white);padding:14px 16px;font-size:7.5px;line-height:11px}
.tab-panel p+p{margin-top:12px}
/* results */
.results-title{position:absolute;left:458px;top:189px;font-size:14px;color:#333;font-weight:400}
.result{position:absolute;left:458px;width:284px;height:19px;background:#e2e2e2}
.result .label{position:absolute;left:0;top:0;width:97px;height:19px;background:var(--navy);color:#fff;font-size:7.5px;padding:4px 6px}
.result .fill{position:absolute;left:97px;top:0;height:19px;background:var(--red);color:#fff;font-size:7.5px;padding:4px 6px}
/* pricing */
.plan{position:absolute;top:391px;width:134px;height:198px;background:var(--white)}
.plan .head{height:23px;background:var(--navy);color:#fff;font-weight:700;font-size:9.5px;padding:5px 13px}
.plan.featured .head,.plan.featured .cta{background:var(--red)}
.plan .price{font-size:13px;color:#333;padding:7px 13px 9px}
.plan .price small{font-size:8.5px}
.plan.featured .price{color:var(--red)}
.plan ul{list-style:none;padding:0 13px}
.plan li{font-size:7.5px;line-height:12px;margin-bottom:13px;display:flex;gap:5px;align-items:center}
.plan.featured li{color:var(--red)}
.plan li svg{width:8px;height:8px;flex:none}
.plan .cta{position:absolute;left:0;bottom:0;width:134px;height:23px;background:var(--navy);color:#fff;font-weight:700;font-size:9.5px;text-align:center;padding-top:5px}
.signup{position:absolute;left:158px;top:614px;width:584px;height:74px;background:var(--white);padding:13px 22px}
.signup h4{font-size:9.5px;font-weight:600;color:#333;margin-bottom:3px}
.signup p{font-size:7.5px;line-height:11px;width:260px}
.signup .email{position:absolute;left:300px;top:22px;width:158px;height:31px;background:#f3f3f3;border:1px solid var(--line)}
.signup .subscribe{position:absolute;left:465px;top:22px;width:104px;height:31px;background:var(--red);color:#fff;text-align:center;line-height:10px;padding-top:4px;font-weight:700;font-size:8px}
.signup .subscribe span{display:block;font-size:13px;line-height:15px}
/* map */
.map{position:absolute;left:0;top:714px;width:900px;height:250px;background:linear-gradient(160deg,#e9e4cf 0%,#dcd9c7 30%,#6d9fe0 55%,#5a8fd8 70%,#e6e2cd 100%)}
.map-title{position:absolute;left:0;top:812px;width:900px;text-align:center;color:rgba(255,255,255,.75);font-weight:800;font-size:46px;letter-spacing:2px}
/* contact */
.contact{position:absolute;left:0;top:964px;width:900px;height:205px;background:var(--white)}
.contact h2{position:absolute;font-size:12.5px;font-weight:600;color:#333}
.field{position:absolute;background:#f3f3f3;border:1px solid #ececec;color:#aaa;font-size:7.5px;font-style:italic;padding:4px 8px}
.send{position:absolute;left:308px;top:156px;width:284px;height:28px;background:var(--red);color:#fff;font-weight:700;font-size:11px;text-align:center;padding-top:6px}
.address{position:absolute;left:608px;top:50px;font-size:7px;line-height:10px}
.address .row{display:flex;gap:8px}
.address .row b{width:6px}
.address a{color:var(--red);text-decoration:none}
.social{position:absolute;left:608px;top:156px;display:flex;gap:4px}
.social span{width:17px;height:17px;display:block}
footer{position:absolute;left:0;top:1169px;width:900px;height:31px;background:var(--navy);color:#b8c1ca;font-size:7px}
footer .copy{position:absolute;left:158px;top:11px}
footer .top{position:absolute;left:672px;top:11px}
footer .top-btn{position:absolute;left:727px;top:8px;width:13px;height:13px;background:rgba(255,255,255,.15)}
</style>
</head>
<body>

<div class="band-grey"></div>

<div class="section-bar" style="top:0">Services<span class="toggle"></span></div>

<div class="services">
  <div class="service">
    <svg viewBox="0 0 26 22"><ellipse cx="10" cy="9" rx="9" ry="7" fill="var(--red)"/><ellipse cx="17" cy="13" rx="8" ry="6" fill="var(--red-dark)"/><path d="M20 17l4 4-1-6z" fill="var(--red-dark)"/></svg>
    <h3>Consulting</h3><p>Have a metal query or sale in mind? Our team gives honest quotes.</p>
  </div>
  <div class="service">
    <svg viewBox="0 0 26 22"><rect x="3" y="2" width="20" height="18" fill="var(--red)"/><path d="M3 8h20M3 14h20M10 2v18M16 2v18" stroke="#fff" stroke-width="1.3"/></svg>
    <h3>Planning</h3><p>Each job is planned with care from pickup to final weighing.</p>
  </div>
  <div class="service">
    <svg viewBox="0 0 26 22"><circle cx="9" cy="13" r="6" fill="none" stroke="var(--red)" stroke-width="3.5" stroke-dasharray="3 1.7"/><circle cx="19" cy="6" r="4" fill="none" stroke="var(--red)" stroke-width="2.8" stroke-dasharray="2.2 1.3"/></svg>
    <h3>Development</h3><p>We keep growing our yard with modern sorting tools and methods.</p>
  </div>
  <div class="service">
    <svg viewBox="0 0 26 22"><path d="M10 1h6v7l6 12H4l6-12z" fill="var(--red)"/></svg>
    <h3>Product</h3><p>Graded ferrous and non-ferrous metal to clear local standards.</p>
  </div>
  <div class="service">
    <svg viewBox="0 0 26 22"><rect x="3" y="2" width="20" height="18" fill="none" stroke="var(--red)" stroke-width="2"/><path d="M8 16v-4M12 16v-7M16 16v-5M20 16V6" stroke="var(--red)" stroke-width="2.3"/></svg>
    <h3>Analysis</h3><p>Every load is tested and weighed so pricing stays fair and clear.</p>
  </div>
  <div class="service">
    <svg viewBox="0 0 26 22"><path d="M2 12l20-9 2 2-9 18-3-1 2-8-6 1-2 3-2-1 1-4z" fill="var(--red)"/></svg>
    <h3>Release</h3><p>Shipments leave on time to buyers here and across the region.</p>
  </div>
</div>

<div class="tabs"><span class="tab active">TAB DATA</span><span class="tab">TAB DATA</span><span class="tab">TAB DATA</span></div>
<div class="tab-panel">
  <p>Suspendisse dictum quam tortor, et dapibus lacus. Quisque euismod lacus in mi consequat sed pulvinar elit ultricies. Nam eu ligula ut massa lobortis scelerisque.</p>
  <p>Curabitur at rhoncus quam. In in tortor quis sem tempor ultricies in eu risus. Fusce posuere justo et metus semper molestie.</p>
</div>

<h2 class="results-title">Some of our results</h2>
<div class="result" style="top:209px"><span class="label">Quisque euismod</span><span class="fill" style="width:164px">80 %</span></div>
<div class="result" style="top:234px"><span class="label">Curabitur at rhonco</span><span class="fill" style="width:49px">30 %</span></div>
<div class="result" style="top:259px"><span class="label">Suspendisse dictum</span><span class="fill" style="width:146px">75 %</span></div>
<div class="result" style="top:284px"><span class="label">Nam eu ligula</span><span class="fill" style="width:116px">60 %</span></div>

<div class="section-bar red" style="top:333px">See our prices and compare!<span class="toggle"></span></div>

<div class="plan" style="left:158px">
  <div class="head">Light</div><div class="price">Free</div>
  <ul>
    <li><svg viewBox="0 0 8 8"><rect x=".5" y=".5" width="7" height="7" fill="none" stroke="currentColor"/><path d="M2 4l1.5 1.5L6 2.5" stroke="currentColor" fill="none"/></svg>Sed laoreet ullamcorper</li>
    <li><svg viewBox="0 0 8 8"><rect x=".5" y=".5" width="7" height="7" fill="none" stroke="currentColor"/><path d="M2 4l1.5 1.5L6 2.5" stroke="currentColor" fill="none"/></svg>Smetus semper molestie</li>
  </ul>
  <div class="cta">Sign up for free</div>
</div>
<div class="plan" style="left:308px">
  <div class="head">Standard</div><div class="price">$ 10 <small>per/m</small></div>
  <ul>
    <li><svg viewBox="0 0 8 8"><rect x=".5" y=".5" width="7" height="7" fill="none" stroke="currentColor"/><path d="M2 4l1.5 1.5L6 2.5" stroke="currentColor" fill="none"/></svg>Sed laoreet ullamcorper</li>
    <li><svg viewBox="0 0 8 8"><rect x=".5" y=".5" width="7" height="7" fill="none" stroke="currentColor"/><path d="M2 4l1.5 1.5L6 2.5" stroke="currentColor" fill="none"/></svg>Smetus semper molestie</li>
    <li><svg viewBox="0 0 8 8"><rect x=".5" y=".5" width="7" height="7" fill="none" stroke="currentColor"/><path d="M2 4l1.5 1.5L6 2.5" stroke="currentColor" fill="none"/></svg>Ametus semper molestie</li>
  </ul>
  <div class="cta">Buy NOW</div>
</div>
<div class="plan featured" style="left:458px">
  <div class="head">Business</div><div class="price">$ 35 <small>per/m</small></div>
  <ul>
    <li><svg viewBox="0 0 8 8"><rect x=".5" y=".5" width="7" height="7" fill="none" stroke="currentColor"/><path d="M2 4l1.5 1.5L6 2.5" stroke="currentColor" fill="none"/></svg>Sed laoreet ullamcorper</li>
    <li><svg viewBox="0 0 8 8"><rect x=".5" y=".5" width="7" height="7" fill="none" stroke="currentColor"/><path d="M2 4l1.5 1.5L6 2.5" stroke="currentColor" fill="none"/></svg>Smetus semper molestie</li>
    <li><svg viewBox="0 0 8 8"><rect x=".5" y=".5" width="7" height="7" fill="none" stroke="currentColor"/><path d="M2 4l1.5 1.5L6 2.5" stroke="currentColor" fill="none"/></svg>Ametus semper molestie</li>
    <li><svg viewBox="0 0 8 8"><rect x=".5" y=".5" width="7" height="7" fill="none" stroke="currentColor"/><path d="M2 4l1.5 1.5L6 2.5" stroke="currentColor" fill="none"/></svg>Qmper molestie</li>
  </ul>
  <div class="cta">Buy NOW</div>
</div>
<div class="plan" style="left:608px">
  <div class="head">Enterprise</div><div class="price">$ 50 <small>per/m</small></div>
  <ul>
    <li><svg viewBox="0 0 8 8"><rect x=".5" y=".5" width="7" height="7" fill="none" stroke="currentColor"/><path d="M2 4l1.5 1.5L6 2.5" stroke="currentColor" fill="none"/></svg>All business options plus</li>
    <li><svg viewBox="0 0 8 8"><rect x=".5" y=".5" width="7" height="7" fill="none" stroke="currentColor"/><path d="M2 4l1.5 1.5L6 2.5" stroke="currentColor" fill="none"/></svg>Smetus semper molestie</li>
    <li><svg viewBox="0 0 8 8"><rect x=".5" y=".5" width="7" height="7" fill="none" stroke="currentColor"/><path d="M2 4l1.5 1.5L6 2.5" stroke="currentColor" fill="none"/></svg>Ametus semper molestie</li>
  </ul>
  <div class="cta">Buy NOW</div>
</div>

<div class="signup">
  <h4>Sign up for free</h4>
  <p>Suspendisse dictum quam tortor, et dapibus lacus. Quisque euismod lacus in mi consequat sed pulvinar elit ultricies. Nam eu ligula ut massa</p>
  <div class="email"></div>
  <div class="subscribe">SUBSCRIBE TO OUR<span>NEWSLETTER</span></div>
</div>

<div class="map" role="img" aria-label="Street map of the yard location in Singapore with waterways and roads"></div>
<div class="map-title">MAP &amp; DIRECTIONS</div>
<div class="section-bar" style="top:714px">Contacts<span class="toggle"></span></div>

<section class="contact">
  <h2 style="left:158px;top:16px">Contact form</h2>
  <div class="field" style="left:158px;top:52px;width:134px;height:19px">name</div>
  <div class="field" style="left:158px;top:86px;width:134px;height:19px">e-mail</div>
  <div class="field" style="left:158px;top:120px;width:134px;height:19px">phone</div>
  <div class="field" style="left:308px;top:52px;width:284px;height:89px">Comment</div>
  <div class="send">SEND</div>
  <h2 style="left:608px;top:16px">Address</h2>
  <div class="address">
    <div>Keng Hoe Metals</div>
    <div style="margin-top:8px">24 Tampines Loop Works Road 3,<br>Singapore 518204</div>
    <div class="row" style="margin-top:8px"><b>t</b>6123 4567</div>
    <div class="row"><b>f</b>6123 4589</div>
    <div class="row" style="margin-top:8px"><b>e</b><a>hello@kenghoemetals.sg</a></div>
  </div>
  <div class="social" aria-label="Social links"><span style="background:#3b5998"></span><span style="background:#d3454a"></span><span style="background:#4aa3df"></span></div>
</section>

<footer>
  <span class="copy">© 2014 KENG HOE METALS</span>
  <span class="top">to top</span>
  <span class="top-btn"></span>
</footer>

</body>
</html>
```